Business Card Design for Kidlarko (Hires out childrens play areas)

Looking to have a business card designed for a company we just bought. The company rents out childrens play areas.

I have uploaded a couple of examples of the kind of business card style I like. Here are two more examples:

https://vesterlingstudio.example.nz/project/brisk-romp-branding/
https://imgvaultcdn.example.com/design_img/8462913/307481/307481_2958174_8462913_a7c3e190_image.jpg

I think a white card will be best due to all the colours in the logo.

Size we require: 3.75" x 2.25" (horizontally orientated) with a 0.125" bleed

Uploaded is two versions of our logo.

Details for the card:
1. My name: Wade Ferrin
2. Title: Managing Director
3. Phone no: 021 537 462
4. Email: wade@kidlarko.example.nz
5. URL: www.kidlarko.example.nz
6. Address:
PO Box 381627
Fernmoor, Auckland

Let me know if you need anything else.

Target Market(s)

Hospitals, doctors surgeries, bed shops, etc.

Contact Information for Business Card

Details for the card:
1. My name: Wade Ferrin
3. Phone no: 021 537 462
5. URL: www.kidlarko.example.nz
6. Address:
PO Box 381627
Fernmoor, Auckland

Requirements
Should not have
• Not too busy.

```html
<!DOCTYPE html>
<html lang="en">
<head>
<meta charset="utf-8">
<title>Kidlarko — Business Card</title>
<link rel="stylesheet" href="https://fonts.googleapis.com/css2?family=Source+Sans+3:wght@400;600;700&display=swap">
<style>
  :root {
    --stage: #e9e7e3;
    --card-white: #ffffff;
    --blue-deep: #0a63c2;
    --blue-mid: #1f86d6;
    --blue-light: #5fc6ee;
    --cyan-edge: #2fd0f5;
    --brand-orange: #f08a1c;
    --brand-dot: #1f86d6;
    --blush: #f6dcec;
    --text-light: #ffffff;
  }
  * { margin: 0; padding: 0; box-sizing: border-box; }
  html, body {
    width: 1200px; height: 1023px; overflow: hidden;
    background: var(--stage);
    font-family: "Source Sans 3", "Myriad Pro", sans-serif;
  }
  .card {
    position: absolute; left: 100px; top: 211px;
    width: 1000px; height: 600px;
    background: var(--card-white);
    overflow: hidden;
    box-shadow: 0 10px 30px rgba(0,0,0,0.18);
  }
  .card-art { position: absolute; inset: 0; }
  .brand {
    position: absolute; left: 55px; top: 215px;
    display: flex; align-items: center; gap: 16px;
  }
  .brand-dot {
    width: 46px; height: 46px; border-radius: 50%;
    background: var(--brand-dot);
  }
  .brand-name {
    font-size: 66px; font-weight: 700; color: var(--brand-orange);
    letter-spacing: 1px; line-height: 1;
  }
  .holder {
    position: absolute; right: 425px; top: 432px;
    color: var(--text-light); text-align: right;
  }
  .holder-name { font-size: 42px; font-weight: 700; line-height: 1.05; white-space: nowrap; }
  .holder-title { font-size: 23px; font-weight: 400; white-space: nowrap; }
  .divider {
    position: absolute; left: 598px; top: 250px;
    width: 2px; height: 190px; background: rgba(255,255,255,0.8);
  }
  .contacts {
    position: absolute; left: 622px; top: 215px;
    list-style: none; color: var(--text-light);
    font-size: 25px; line-height: 1.2;
  }
  .contacts li { display: flex; align-items: center; gap: 12px; margin-bottom: 6px; white-space: nowrap; }
  .contacts .no-icon { padding-left: 38px; }
  .icon {
    width: 26px; height: 26px; flex: none;
    background: var(--text-light); border-radius: 5px;
    display: flex; align-items: center; justify-content: center;
  }
  .icon svg { width: 18px; height: 18px; }
</style>
</head>
<body>
<main class="card">
  <svg class="card-art" viewBox="0 0 1000 600" width="1000" height="600">
    <defs>
      <linearGradient id="waveFill" x1="0" y1="1" x2="1" y2="0">
        <stop offset="0" stop-color="var(--blue-light)"/>
        <stop offset="0.45" stop-color="var(--blue-mid)"/>
        <stop offset="1" stop-color="var(--blue-deep)"/>
      </linearGradient>
      <radialGradient id="blushFill" cx="0.5" cy="0.5" r="0.5">
        <stop offset="0" stop-color="var(--blush)" stop-opacity="0.9"/>
        <stop offset="1" stop-color="var(--blush)" stop-opacity="0"/>
      </radialGradient>
    </defs>
    <ellipse class="mascot-watermark" role="img" aria-label="Faint brand mascot watermark area" cx="720" cy="40" rx="190" ry="130" fill="url(#blushFill)"/>
    <path class="wave-edge" d="M0,530 C200,500 330,430 440,300 C540,185 620,50 740,0 L1000,0 L1000,600 L0,600 Z" fill="var(--cyan-edge)"/>
    <path class="wave-band" d="M0,560 C210,525 350,450 460,320 C560,200 640,60 770,0 L1000,0 L1000,600 L0,600 Z" fill="url(#waveFill)"/>
    <path class="wave-line" d="M0,545 C205,512 340,440 450,310 C550,192 630,55 755,0" fill="none" stroke="#ffffff" stroke-width="3"/>
  </svg>

  <div class="brand">
    <span class="brand-dot"></span>
    <span class="brand-name">Kidlarko</span>
  </div>

  <div class="holder">
    <p class="holder-name">Wade Ferrin</p>
    <p class="holder-title">Managing Director</p>
  </div>

  <span class="divider"></span>

  <ul class="contacts">
    <li><span class="icon"><svg viewBox="0 0 24 24"><path d="M6.6 10.8a15 15 0 0 0 6.6 6.6l2.2-2.2a1 1 0 0 1 1-.25 11 11 0 0 0 3.6.6 1 1 0 0 1 1 1V20a1 1 0 0 1-1 1A17 17 0 0 1 3 4a1 1 0 0 1 1-1h3.5a1 1 0 0 1 1 1 11 11 0 0 0 .6 3.6 1 1 0 0 1-.25 1z" fill="var(--blue-mid)"/></svg></span>021 537 462</li>
    <li><span class="icon"><svg viewBox="0 0 24 24"><rect x="3" y="6" width="18" height="12" rx="1.5" fill="none" stroke="var(--blue-mid)" stroke-width="2"/><path d="M3 7l9 6 9-6" fill="none" stroke="var(--blue-mid)" stroke-width="2"/></svg></span>wade@kidlarko.example.nz</li>
    <li><span class="icon"><svg viewBox="0 0 24 24"><circle cx="12" cy="12" r="8.5" fill="none" stroke="var(--blue-mid)" stroke-width="2"/><path d="M3.5 12h17M12 3.5c3 3 3 14 0 17M12 3.5c-3 3-3 14 0 17" fill="none" stroke="var(--blue-mid)" stroke-width="1.6"/></svg></span>www.kidlarko.example.nz</li>
    <li><span class="icon"><svg viewBox="0 0 24 24"><path d="M12 2a7 7 0 0 0-7 7c0 5 7 13 7 13s7-8 7-13a7 7 0 0 0-7-7z" fill="var(--blue-mid)"/><circle cx="12" cy="9" r="2.6" fill="#fff"/></svg></span>PO Box 381627</li>
    <li class="no-icon">Fernmoor, Auckland</li>
  </ul>
</main>
</body>
</html>
```